Consulting company, design, Interior design in commercial real estate (Tertiai sector *

Company name: DORALYNE: from the Greek Evexia well-being, was born from a desire to combine well-being and work. By the choice of design, materials, design and furniture, everything is thought from this perspective

Logo: Essay with Möbius Ribbon and / or with the infinite acronym / and or triangle ...
Sentences to write:
"The exclusive partner for your development projects"
"Consulting - Design - Construction"
"We manage EVERYTHING for you"

On the back: Photo (attached; if photo is not clear, another photo can be provided) with company name and "DORALYNE, Excellence and reliability"
My name / First name: provided later (double name), Manager
Address: supplied later
Tel: supplied later
Website: www. doralyne.example
Colors: Black, gold and white. Other admissible colors
See attached files

Target Market(s)

Real estate business

Contact Information for Business Card

Nom de l'entreprise : DORALYNE : du grec Evexia bien être, est né d'une volonté de faire rimer bien être et travail. Par le choix de la conception, des matériaux, du design et du mobilier, tout est pensé dans cette optique

Logo : Essai avec Ruban de Möbius et /ou avec le sigle infini / et ou triangle...
Phrases à inscrire :
"Le partenaire exclusif de vos projets d'aménagement"
"Conseil - Conception - Construction"
"Nous gérons TOUT pour vous"

Au verso : Photo (ci-jointe ; si photo pas nette, une autre photo peut être fournie) avec nom de l'entreprise et Mention "DORALYNE, Excellence et fiabilité"
Mon nom / Prénom : fourni ultérieurement (prénom double), Gérant
Adresse : fourni ultérieurement
Tél : fourni ultérieurement
Site Web : www. doralyne.example
Couleurs : Noir, doré et blanc. Autre couleurs recevables
Voir fichiers ci-joint

Requirements
Must have
• My project must be simple, clear, neat and design.
The business card must catch the customer

```html
<!DOCTYPE html>
<html lang="fr">
<head>
<meta charset="utf-8">
<title>DORALYNE – Carte de visite</title>
<link rel="stylesheet" href="https://fonts.googleapis.com/css2?family=Poppins:wght@400;500;600;700&display=swap">
<style>
  :root {
    --stage: #e9e9e7;
    --card-white: #ffffff;
    --card-dark: #232323;
    --ink: #111111;
    --gold: #f0b323;
    --silver: #e6e6e6;
    --rule: #7a7a7a;
  }
  * { box-sizing: border-box; margin: 0; padding: 0; }
  html, body {
    width: 1200px; height: 900px; overflow: hidden;
    background: var(--stage);
    font-family: "Poppins", sans-serif;
  }
  .sheet {
    width: 1200px; height: 900px;
    display: flex; flex-direction: column; align-items: center; justify-content: center;
    gap: 40px;
  }
  .card {
    width: 640px; height: 366px;
    position: relative;
    box-shadow: 0 10px 30px rgba(0,0,0,.18);
  }
  /* Front */
  .card--front { background: var(--card-white); display: flex; align-items: center; }
  .brand { display: flex; flex-direction: column; align-items: center; }
  .card--front .brand { width: 330px; }
  .brand__row { display: flex; align-items: center; gap: 12px; }
  .brand__square { width: 14px; height: 14px; background: var(--gold); }
  .brand__name {
    font-weight: 500; font-size: 38px; letter-spacing: 9px; color: var(--ink);
  }
  .brand__tagline {
    margin-top: 6px; font-size: 9.5px; font-weight: 500; letter-spacing: 2.2px;
    color: var(--gold); text-transform: uppercase;
  }
  .divider { width: 1px; height: 190px; background: var(--rule); }
  .contact { padding-left: 34px; color: var(--ink); }
  .contact__name { font-weight: 700; font-size: 21px; line-height: 1.1; }
  .contact__role { color: var(--gold); font-size: 15px; margin-bottom: 14px; }
  .contact__list { list-style: none; font-size: 13px; line-height: 1.45; }
  .contact__item { display: flex; align-items: flex-start; gap: 8px; margin-bottom: 3px; }
  .contact__item svg { width: 13px; height: 13px; flex: none; margin-top: 3px; fill: var(--gold); }
  /* Back */
  .card--back {
    background: var(--card-dark);
    display: flex; flex-direction: column; align-items: center; justify-content: center;
  }
  .card--back .brand__name { color: var(--silver); font-size: 44px; letter-spacing: 11px; }
  .card--back .brand__tagline { font-size: 10.5px; }
  .back__web { margin-top: 36px; color: var(--silver); font-size: 15px; letter-spacing: .5px; }
</style>
</head>
<body>
<main class="sheet">
  <section class="card card--front" aria-label="Recto">
    <div class="brand">
      <div class="brand__row">
        <span class="brand__square"></span>
        <span class="brand__name">DORALYNE</span>
      </div>
      <p class="brand__tagline">Consulting - Design - Construction</p>
    </div>
    <div class="divider"></div>
    <div class="contact">
      <p class="contact__name">Fourni ultérieurement</p>
      <p class="contact__role">Gérant</p>
      <ul class="contact__list">
        <li class="contact__item">
          <svg viewBox="0 0 24 24"><path d="M6.6 10.8a15 15 0 006.6 6.6l2.2-2.2c.3-.3.7-.4 1-.2 1.1.4 2.3.6 3.6.6.6 0 1 .4 1 1V20c0 .6-.4 1-1 1A17 17 0 013 4c0-.6.4-1 1-1h3.5c.6 0 1 .4 1 1 0 1.3.2 2.5.6 3.6.1.3 0 .7-.2 1z"/></svg>
          <span>0155-2468-3570</span>
        </li>
        <li class="contact__item">
          <svg viewBox="0 0 24 24"><path d="M2 5h20v14H2z M2 5l10 8 10-8" fill="none" stroke="#f0b323" stroke-width="2.4"/></svg>
          <span>info@doralyne.example</span>
        </li>
        <li class="contact__item">
          <svg viewBox="0 0 24 24"><circle cx="12" cy="12" r="9.5" fill="none" stroke="#f0b323" stroke-width="2"/><path d="M2.5 12h19M12 2.5c3 3 3 16 0 19M12 2.5c-3 3-3 16 0 19" fill="none" stroke="#f0b323" stroke-width="1.6"/></svg>
          <span>www. doralyne.example</span>
        </li>
        <li class="contact__item">
          <svg viewBox="0 0 24 24"><path d="M12 2a7 7 0 00-7 7c0 5 7 13 7 13s7-8 7-13a7 7 0 00-7-7zm0 9.5A2.5 2.5 0 1112 6.5a2.5 2.5 0 010 5z"/></svg>
          <span>118 Larkfield Road<br>Suite 210, Brenmoor<br>ST 40217</span>
        </li>
      </ul>
    </div>
  </section>

  <section class="card card--back" aria-label="Verso">
    <div class="brand">
      <div class="brand__row">
        <span class="brand__square"></span>
        <span class="brand__name">DORALYNE</span>
      </div>
      <p class="brand__tagline">Consulting - Design - Construction</p>
    </div>
    <p class="back__web">www. doralyne.example</p>
  </section>
</main>
</body>
</html>
```